Wine Label Design

Organization name: Halvern Wine Company

My company is called Halvern Wine Company, I’m a wine importer and wholesaler who distributes wine domestically.

We are about to launch a line of three premium and one sparkling wine that we will wholesale to various retailers, wine stores, and restaurants for re-sale. The wines label will have “Dorian Halvern” I plan on having the labels the same and just changing the varietal as needed. My wine are made from premium grapes and will be marketed as a high end wine. My current label size is 3 1/2" wide by 5" in long and the labels can be on a solid background or transparent.

I would like the first label to be for my Cabernet Sauvignon, California, 2012, 750ML (for the size of the bottle) and ALC 13.8% BY VOL (for the alcohol content).

Colors: I am open to any and all designs that would alter my perception of what will be best!

Further:
Current label is boring and poorly done, so hopefully you designers can come up with something better

Industry/Entity Type

It Company

```html
<!DOCTYPE html>
<html lang="en">
<head>
<meta charset="utf-8">
<title>Dorian Halvern – Wine Label Series</title>
<link rel="stylesheet" href="https://fonts.googleapis.com/css2?family=Cinzel:wght@400;500&family=Pinyon+Script&display=swap">
<style>
  :root {
    --page: #ffffff;
    --label-black: #000000;
    --frame-outer: #1a1a1a;
    --frame-light: #d8d8d8;
    --frame-mid: #8c8c8c;
    --name-white: #ffffff;
    --name-grey: #8e8e8e;
    --small-text: #e6e6e6;
    --accent-cab: #4fb6d8;
    --accent-cab-deep: #0e3a4e;
    --accent-neb: #e0982e;
    --accent-neb-deep: #4a2a05;
    --accent-pinot: #e3343a;
    --accent-pinot-deep: #4a0508;
  }
  html, body {
    margin: 0;
    padding: 0;
    width: 1200px;
    height: 1000px;
    overflow: hidden;
    background: var(--page);
  }
  .series {
    position: relative;
    width: 1200px;
    height: 1000px;
  }
  .label {
    position: absolute;
    top: 448px;
    width: 376px;
    height: 538px;
    box-sizing: border-box;
    background: var(--label-black);
    border: 2px solid var(--frame-outer);
    font-family: "Cinzel", "Times New Roman", serif;
    text-align: center;
    color: var(--name-white);
  }
  .label::before,
  .label::after {
    content: "";
    position: absolute;
    pointer-events: none;
  }
  .label::before {
    inset: 4px;
    border: 2px solid var(--frame-light);
  }
  .label::after {
    inset: 10px;
    border: 1px solid var(--frame-mid);
  }
  .label--cabernet { left: 11px;  --accent: var(--accent-cab);   --accent-deep: var(--accent-cab-deep); }
  .label--nebbiolo { left: 411px; --accent: var(--accent-neb);   --accent-deep: var(--accent-neb-deep); }
  .label--pinot    { left: 811px; --accent: var(--accent-pinot); --accent-deep: var(--accent-pinot-deep); }

  .emblem {
    position: absolute;
    left: 107px;
    top: 78px;
    width: 158px;
    height: 158px;
    border-radius: 50%;
    box-sizing: border-box;
    border: 2px solid var(--frame-light);
    padding: 4px;
  }
  .emblem__art {
    width: 100%;
    height: 100%;
    border-radius: 50%;
    background: radial-gradient(circle at 40% 55%, var(--accent) 0%, var(--accent-deep) 75%);
  }
  .brand-first,
  .brand-last,
  .region,
  .varietal,
  .vintage {
    position: absolute;
    left: 0;
    right: 0;
    margin: 0;
    line-height: 1;
    font-weight: 400;
  }
  .brand-first {
    top: 246px;
    font-size: 40px;
    letter-spacing: 10px;
    padding-left: 10px;
    color: var(--name-white);
  }
  .brand-last {
    top: 296px;
    font-size: 32px;
    letter-spacing: 9px;
    padding-left: 9px;
    color: var(--name-grey);
  }
  .region {
    top: 344px;
    font-family: "Pinyon Script", cursive;
    font-size: 29px;
    color: var(--accent);
  }
  .varietal {
    top: 403px;
    font-size: 16px;
    letter-spacing: 1px;
    color: var(--small-text);
  }
  .vintage {
    top: 431px;
    font-size: 24px;
    color: var(--small-text);
  }
  .fine-print {
    position: absolute;
    left: 24px;
    right: 24px;
    bottom: 20px;
    display: flex;
    justify-content: space-between;
    font-family: Arial, Helvetica, sans-serif;
    font-size: 10px;
    color: var(--small-text);
  }
</style>
</head>
<body>
<main class="series">

  <article class="label label--cabernet">
    <div class="emblem"><div class="emblem__art" role="img" aria-label="Blue swirling wave artwork in a round medallion"></div></div>
    <h1 class="brand-first">DORIAN</h1>
    <p class="brand-last">HALVERN</p>
    <p class="region">California</p>
    <p class="varietal">CABERNET SAUVIGNON</p>
    <p class="vintage">2012</p>
    <div class="fine-print"><span>750ML</span><span>ALC 13.8% BY VOL</span></div>
  </article>

  <article class="label label--nebbiolo">
    <div class="emblem"><div class="emblem__art" role="img" aria-label="Amber swirling wave artwork in a round medallion"></div></div>
    <h1 class="brand-first">DORIAN</h1>
    <p class="brand-last">HALVERN</p>
    <p class="region">California</p>
    <p class="varietal">NEBBIOLO</p>
    <p class="vintage">2012</p>
    <div class="fine-print"><span>750ML</span><span>ALC 13.8% BY VOL</span></div>
  </article>

  <article class="label label--pinot">
    <div class="emblem"><div class="emblem__art" role="img" aria-label="Red swirling wave artwork in a round medallion"></div></div>
    <h1 class="brand-first">DORIAN</h1>
    <p class="brand-last">HALVERN</p>
    <p class="region">California</p>
    <p class="varietal">PINOT NOIR</p>
    <p class="vintage">2012</p>
    <div class="fine-print"><span>750ML</span><span>ALC 13.8% BY VOL</span></div>
  </article>

</main>
</body>
</html>
```